New Business Card Design Project

New business card design required for an electrical business in Australia. Offering quality electrical services including design and installation. Electrical services offered are domestic, commercial and industrial. Also meets all the air conditioning installation and maintenance needs.

Target Market(s)

The business is sleek, professional and caters primarily to wealthy clients and government contracts looking for exceptional, tailored service.

Industry/Entity Type

Electrical

Contact Information for Business Card

Gareth Pollwick (Director)
0438 692 174
admin@rvoelectrical.com.au
www.rvoelectrical.com.au

Font styles to use
Sans Serif

Requirements
Must have
• The business card must show the license number - 64139 to comply with legislation.
Nice to have
• The logo colours and fonts could be incorporated into the design if the designer sees fit. We are open to new ideas and welcome creativity. The logo style guide is attached for reference if required.

```html
<!DOCTYPE html>
<html lang="en">
<head>
<meta charset="utf-8">
<title>RVO Electrical – Business Cards</title>
<link rel="stylesheet" href="https://fonts.googleapis.com/css2?family=Arimo:wght@400;700&display=swap">
<style>
  :root {
    --navy: #142b55;
    --white: #ffffff;
    --paper: #fbfbfc;
    --grey: #6b6f78;
    --backdrop: #2a2a2a;
  }
  * { margin: 0; padding: 0; box-sizing: border-box; }
  html, body { width: 1200px; height: 1015px; overflow: hidden; }
  body {
    background: var(--backdrop);
    font-family: "Arimo", Arial, sans-serif;
    position: relative;
  }
  .card {
    position: absolute;
    left: 220px;
    width: 760px;
    height: 434px;
    overflow: hidden;
    box-shadow: 0 12px 30px rgba(0,0,0,.45);
  }
  .card--back { top: 44px; background: var(--navy); }
  .card--front { top: 530px; background: var(--paper); }
  .card__wave { position: absolute; inset: 0; width: 100%; height: 100%; }

  .wordmark {
    position: absolute;
    display: flex;
    align-items: center;
    gap: 14px;
    font-weight: 700;
    letter-spacing: 3px;
    white-space: nowrap;
  }
  .wordmark__name { font-size: 58px; line-height: 1; }
  .wordmark__trade { font-size: 58px; line-height: 1; }
  .wordmark__dot {
    width: 14px; height: 14px; border-radius: 50%;
  }
  .card--back .wordmark { left: 110px; top: 110px; color: var(--white); font-size: 40px; }
  .card--back .wordmark__name,
  .card--back .wordmark__trade { font-size: 40px; }
  .card--back .wordmark__dot { background: var(--white); }
  .card--front .wordmark { right: 40px; top: 70px; color: var(--navy); }
  .card--front .wordmark__name,
  .card--front .wordmark__trade { font-size: 34px; }
  .card--front .wordmark__dot { background: var(--navy); }

  .licence {
    position: absolute;
    left: 70px; bottom: 56px;
    color: var(--navy);
    font-weight: 700;
    font-size: 20px;
    letter-spacing: .5px;
  }

  .holder { position: absolute; left: 56px; top: 74px; }
  .holder__name { color: var(--navy); font-weight: 700; font-size: 25px; letter-spacing: .5px; }
  .holder__role { color: var(--grey); font-size: 21px; margin-top: 2px; letter-spacing: .5px; }

  .contacts {
    position: absolute;
    left: 214px; bottom: 32px;
    list-style: none;
    color: var(--white);
    font-size: 22px;
  }
  .contacts__item { display: flex; align-items: center; gap: 12px; margin-top: 6px; }
  .contacts__icon { width: 20px; height: 20px; flex: none; }
</style>
</head>
<body>

  <section class="card card--back" aria-label="Business card back">
    <svg class="card__wave" viewBox="0 0 760 434" preserveAspectRatio="none" aria-hidden="true">
      <path fill="var(--paper)" d="M0 434 L0 400 C60 330 160 300 330 272 C540 238 700 210 760 60 L760 434 Z"/>
      <path fill="none" stroke="var(--navy)" stroke-width="5" d="M300 290 C520 250 690 225 748 80"/>
      <path fill="none" stroke="var(--navy)" stroke-width="2.5" d="M420 262 C600 236 712 214 756 110"/>
    </svg>
    <div class="wordmark">
      <span class="wordmark__name">RVO</span>
      <span class="wordmark__trade">ELECTRICAL</span>
      <span class="wordmark__dot"></span>
    </div>
    <p class="licence">LIC NO: 64139</p>
  </section>

  <section class="card card--front" aria-label="Business card front">
    <svg class="card__wave" viewBox="0 0 760 434" preserveAspectRatio="none" aria-hidden="true">
      <path fill="var(--navy)" d="M0 434 L0 400 C60 320 170 292 340 266 C550 236 700 215 760 70 L760 434 Z"/>
      <path fill="none" stroke="var(--navy)" stroke-width="5" d="M330 250 C540 222 700 200 748 56"/>
      <path fill="none" stroke="var(--navy)" stroke-width="2.5" d="M440 228 C610 206 712 186 752 36"/>
    </svg>
    <div class="holder">
      <p class="holder__name">GARETH POLLWICK</p>
      <p class="holder__role">DIRECTOR</p>
    </div>
    <div class="wordmark">
      <span class="wordmark__name">RVO</span>
      <span class="wordmark__trade">ELECTRICAL</span>
      <span class="wordmark__dot"></span>
    </div>
    <ul class="contacts">
      <li class="contacts__item">
        <svg class="contacts__icon" viewBox="0 0 24 24" aria-hidden="true"><path fill="var(--white)" d="M6.6 10.8a15.1 15.1 0 0 0 6.6 6.6l2.2-2.2a1 1 0 0 1 1-.25 11.4 11.4 0 0 0 3.6.57 1 1 0 0 1 1 1V20a1 1 0 0 1-1 1A17 17 0 0 1 3 4a1 1 0 0 1 1-1h3.5a1 1 0 0 1 1 1c0 1.25.2 2.45.57 3.57a1 1 0 0 1-.25 1z"/></svg>
        <span>0438 692 174</span>
      </li>
      <li class="contacts__item">
        <svg class="contacts__icon" viewBox="0 0 24 24" aria-hidden="true"><rect x="2" y="5" width="20" height="14" fill="none" stroke="var(--white)" stroke-width="2"/><path d="M2 5l10 8 10-8" fill="none" stroke="var(--white)" stroke-width="2"/></svg>
        <span>admin@rvoelectrical.com.au</span>
      </li>
      <li class="contacts__item">
        <svg class="contacts__icon" viewBox="0 0 24 24" aria-hidden="true"><g fill="none" stroke="var(--white)" stroke-width="1.8"><circle cx="12" cy="12" r="10"/><ellipse cx="12" cy="12" rx="4.5" ry="10"/><path d="M2 12h20M4 7h16M4 17h16"/></g></svg>
        <span>www.rvoelectrical.com.au</span>
      </li>
    </ul>
  </section>

</body>
</html>
```